Geschäftspapiere für Unternehmen aus Not- und Sicherheitsbeleuchtungsbranche
Zielgruppe
Wir sind ein Unternehmen der Not- und Sicherheitsbeleuchtungsbranche und arbeiten vornehmlich mit dem deutschen Elektrogroßhandel zusammen.
Aufgabenstellung
WIr möchten nicht nur Schreibblöcke drucken, wir benötigen die Vorlage auch als Word-Datei für Geschäftsbriefe.
Orientierung und Farbwahl gemäß unserer Website. Im Anhang finden Sie bereits das aktuelle Briefdesign. Dieses verbraucht jedoch zu viel Platz und liegt uns nicht als Word vor. Die Daten können übernommen werden, ergänzt muss noch die UST-ID werden: DE718206359

```html
<!DOCTYPE html>
<html lang="de">
<head>
<meta charset="utf-8">
<title>Lumora Systems – Briefbogen</title>
<link rel="stylesheet" href="https://fonts.googleapis.com/css2?family=Figtree:wght@400;500;700&display=swap">
<style>
  :root {
    --backdrop-top: #7f7770;
    --backdrop-bottom: #8c9aa1;
    --paper: #ffffff;
    --brand-magenta: #b0005f;
    --brand-grey: #5f676d;
    --ink: #1e1e1e;
    --grid-line: #dcdcdc;
  }
  * { margin: 0; padding: 0; box-sizing: border-box; }
  html, body { width: 887px; height: 1200px; overflow: hidden; }
  body {
    background: linear-gradient(180deg, var(--backdrop-top), var(--backdrop-bottom));
    font-family: "Figtree", Arial, sans-serif;
    position: relative;
  }
  .letterhead {
    position: absolute;
    left: 54px; top: 62px;
    width: 776px; height: 1098px;
    background: var(--paper);
  }
  .brand {
    position: absolute;
    left: 48px; top: 46px;
    display: flex; align-items: center; gap: 12px;
  }
  .brand-square {
    width: 34px; height: 34px;
    background: var(--brand-magenta);
  }
  .brand-name {
    font-size: 34px; font-weight: 500;
    letter-spacing: 3px;
    color: var(--brand-grey);
  }
  .divider {
    position: absolute;
    top: 37px; width: 1.5px; height: 67px;
    background: var(--brand-grey);
  }
  .divider--address { left: 364px; }
  .divider--contact { left: 527px; }
  .address {
    position: absolute;
    left: 379px; top: 44px;
    font-size: 11.5px; line-height: 16px;
    color: var(--ink);
    font-style: normal;
  }
  .address .company { color: var(--brand-magenta); font-weight: 700; }
  .contact {
    position: absolute;
    left: 547px; top: 44px;
    list-style: none;
    font-size: 11.5px; line-height: 16px;
    color: var(--ink);
  }
  .contact li { display: flex; align-items: center; gap: 8px; }
  .contact svg { width: 11px; height: 11px; fill: var(--brand-magenta); flex: none; }
  .writing-grid { position: absolute; left: 0; top: 0; }
</style>
</head>
<body>
  <main class="letterhead">
    <div class="brand">
      <span class="brand-square"></span>
      <span class="brand-name">LUMORA</span>
    </div>

    <span class="divider divider--address"></span>
    <address class="address">
      <div class="company">Lumora Systems GmbH</div>
      <div>Lindenweg 14</div>
      <div>D-84032 Altdorf</div>
    </address>

    <span class="divider divider--contact"></span>
    <ul class="contact">
      <li>
        <svg viewBox="0 0 12 12" aria-hidden="true"><path d="M2.5 0.8 4.3 0.5 5.2 3.2 4 4.2C4.6 5.7 5.8 7 7.3 7.8L8.4 6.8 11 7.9 10.7 9.7C10.5 10.6 9.7 11.1 8.8 10.9 4.9 10 1.8 6.8 1.1 2.8 0.9 1.8 1.6 1 2.5 0.8Z"/></svg>
        <span>08731 40267 19</span>
      </li>
      <li>
        <svg viewBox="0 0 12 12" aria-hidden="true"><path d="M0.5 2.5h11v7h-11z M0.5 2.8 6 6.8 11.5 2.8" stroke="#fff" stroke-width="0.9"/></svg>
        <span>info@lumora-systems.de</span>
      </li>
      <li>
        <svg viewBox="0 0 12 12" aria-hidden="true"><circle cx="6" cy="6" r="5.2" fill="none" stroke="var(--brand-magenta)" stroke-width="1"/><ellipse cx="6" cy="6" rx="2.3" ry="5.2" fill="none" stroke="var(--brand-magenta)" stroke-width="0.9"/><path d="M0.8 6h10.4M1.6 3.5h8.8M1.6 8.5h8.8" stroke="var(--brand-magenta)" stroke-width="0.9"/></svg>
        <span>www.lumora-systems.de</span>
      </li>
    </ul>

    <svg class="writing-grid" width="776" height="1098" viewBox="0 0 776 1098" aria-hidden="true">
      <defs>
        <pattern id="grid-rows" x="54" y="166" width="20" height="15.2" patternUnits="userSpaceOnUse">
          <line x1="0" y1="0.3" x2="20" y2="0.3" stroke="var(--grid-line)" stroke-width="0.6"/>
        </pattern>
        <pattern id="grid-cols" x="79" y="0" width="15.2" height="20" patternUnits="userSpaceOnUse">
          <line x1="0.3" y1="0" x2="0.3" y2="20" stroke="var(--grid-line)" stroke-width="0.6"/>
        </pattern>
      </defs>
      <rect x="54" y="166" width="657" height="882" fill="url(#grid-rows)"/>
      <rect x="79" y="142" width="623" height="920" fill="url(#grid-cols)"/>
    </svg>
  </main>
</body>
</html>
```